Inspiration Poster

Inspirational Poster that has a Kamran Dulo like abstract look (http://www.vexalo.com/images/search?q=kamran+dulo&FORM=HDRSC2) with the text:

"we walk not in order to arrive at the promise land but because walking itself is a revolution"
-Peter Ambrick

```html
<!DOCTYPE html>
<html lang="en">
<head>
<meta charset="utf-8">
<title>Walking Itself Is a Revolution — Poster</title>
<link rel="stylesheet" href="https://fonts.googleapis.com/css2?family=Petit+Formal+Script&display=swap">
<style>
  :root {
    --plank-tan: #c49e4f;
    --plank-light: #d5b968;
    --plank-warm: #caa04d;
    --plank-coral: #e0734a;
    --plank-red: #e4694b;
    --seam: #5a3a1c;
    --ink: #111008;
    --silhouette-dark: rgba(27, 20, 11, 0.82);
    --silhouette-fade: rgba(27, 20, 11, 0.45);
    --splash: rgba(44, 240, 122, 0.55);
    --splash-fade: rgba(44, 240, 122, 0);
  }
  html, body {
    margin: 0;
    padding: 0;
    width: 1200px;
    height: 843px;
    overflow: hidden;
    background: var(--plank-tan);
  }
  .poster {
    position: relative;
    width: 1200px;
    height: 843px;
    overflow: hidden;
  }
  .planks {
    position: absolute;
    inset: 0;
  }
  .tree-art {
    position: absolute;
    left: 0;
    top: 0;
    width: 500px;
    height: 843px;
    background: linear-gradient(to right, var(--silhouette-dark), var(--silhouette-fade));
  }
  .splash {
    position: absolute;
  }
  .splash--ground {
    left: 0;
    bottom: 0;
    width: 420px;
    height: 180px;
    background: linear-gradient(to top, var(--splash), var(--splash-fade));
  }
  .splash--sky {
    right: 0;
    top: 0;
    width: 560px;
    height: 420px;
    background: linear-gradient(to bottom left, var(--splash), var(--splash-fade) 70%);
    opacity: 0.6;
  }
  .quote {
    position: absolute;
    left: 400px;
    top: 92px;
    width: 800px;
    margin: 0;
    font-family: "Petit Formal Script", cursive;
    font-size: 54px;
    line-height: 97px;
    color: var(--ink);
    text-align: center;
    word-spacing: 6px;
  }
  .quote__line { display: block; white-space: nowrap; }
  .quote__mark { font-size: 72px; line-height: 0; }
  .author {
    position: absolute;
    left: 505px;
    top: 650px;
    width: 600px;
    margin: 0;
    font-family: "Petit Formal Script", cursive;
    font-size: 54px;
    color: var(--ink);
    text-align: center;
  }
</style>
</head>
<body>
<main class="poster">
  <svg class="planks" width="1200" height="843" viewBox="0 0 1200 843" aria-hidden="true">
    <rect x="0" y="0" width="263" height="843" fill="var(--plank-tan)"/>
    <rect x="263" y="0" width="137" height="843" fill="var(--plank-coral)"/>
    <rect x="400" y="0" width="255" height="843" fill="var(--plank-light)"/>
    <rect x="655" y="0" width="140" height="843" fill="var(--plank-red)"/>
    <rect x="795" y="0" width="270" height="843" fill="var(--plank-warm)"/>
    <rect x="1065" y="0" width="135" height="843" fill="var(--plank-red)"/>
    <g stroke="var(--seam)" stroke-width="2">
      <line x1="263" y1="0" x2="263" y2="843"/>
      <line x1="400" y1="0" x2="400" y2="843"/>
      <line x1="655" y1="0" x2="655" y2="843"/>
      <line x1="795" y1="0" x2="795" y2="843"/>
      <line x1="1065" y1="0" x2="1065" y2="843"/>
      <line x1="0" y1="662" x2="400" y2="662"/>
      <line x1="655" y1="178" x2="795" y2="178"/>
      <line x1="1065" y1="662" x2="1200" y2="662"/>
    </g>
  </svg>

  <div class="splash splash--sky" role="img" aria-label="Bright green paint splatters across the upper right"></div>
  <div class="tree-art" role="img" aria-label="Black silhouette of a leaning tree with birds in its branches and a hummingbird in flight"></div>
  <div class="splash splash--ground" role="img" aria-label="Bright green grass-like paint splatters at the base of the tree"></div>

  <blockquote class="quote">
    <span class="quote__line"><span class="quote__mark">“</span>We walk not in</span>
    <span class="quote__line">order to arrive at the</span>
    <span class="quote__line">promise land but</span>
    <span class="quote__line">because walking itself</span>
    <span class="quote__line">is a revolution<span class="quote__mark">”</span></span>
  </blockquote>
  <p class="author">Peter Ambrick</p>
</main>
</body>
</html>
```